Business Card Design Project

I would like to have a project of business card with incorporated attachted logo elements in warm colors like: gold, yellow, brown.
We would like incorporate below information into the design
Name of the Company: Continental Hoop Invitational
Name: Dorian Pelkey
Position: Project Director
e-mail: dorian@hoopinvitational.net
mobile: +65 83147092
website: www.hoopinvitational.net
Address: 47 Marbury Lane, #06-11, Singapore 915274
There is a picture attachted which can be used as a back side of the buisness card - we would like to follow the colors theme on the front card ( with the person contact details) how ever the front card we will prefer with white background but with graphfic elements coming from logo.
Project Deadline Extended
Reason: the project has been launched on 24 of April with deadline by 24 of April by mistakes. Thats why I would like to extend the deadline.
Name: Dorian Pelkey
mobile: +65 83147092

```html
<!DOCTYPE html>
<html lang="en">
<head>
<meta charset="utf-8">
<title>Continental Hoop Invitational – Business Cards</title>
<link href="https://fonts.googleapis.com/css2?family=Roboto+Condensed:wght@400;700&display=swap" rel="stylesheet">
<style>
  :root {
    --backdrop: #e8e8e8;
    --card-white: #ffffff;
    --ring-grey: #a3a3a3;
    --ink: #2a2a2a;
    --ink-soft: #444444;
    --brand-purple: #6a2aa8;
    --purple-1: #a53fdc;
    --purple-2: #8e33c8;
    --purple-3: #7a2cb4;
    --purple-4: #63279c;
    --purple-5: #4b2386;
    --gold-1: #c5a670;
    --gold-2: #ad8a55;
    --gold-3: #937040;
    --gold-4: #77552c;
    --gold-5: #5a3a14;
  }
  html, body {
    margin: 0;
    width: 1200px;
    height: 1198px;
    overflow: hidden;
    background: var(--backdrop);
  }
  .canvas {
    position: relative;
    width: 1200px;
    height: 1198px;
  }
  .card {
    position: absolute;
    width: 520px;
    height: 360px;
    border-radius: 14px;
    overflow: hidden;
    box-shadow: 0 4px 14px rgba(0,0,0,0.22);
    font-family: "Roboto Condensed", "Arial Narrow", sans-serif;
    color: var(--ink);
  }
  .card--purple { left: 150px; top: 210px; }
  .card--gold { left: 500px; top: 520px; }
  .card__art {
    position: absolute;
    inset: 0;
    width: 520px;
    height: 360px;
  }
  .card__content {
    position: absolute;
    left: 48px;
    top: 52px;
  }
  .brand {
    display: flex;
    align-items: center;
    gap: 8px;
    width: 150px;
  }
  .brand__dot {
    flex: none;
    width: 14px;
    height: 14px;
    border-radius: 50%;
    background: var(--brand-purple);
  }
  .brand__name {
    font-weight: 700;
    font-size: 15px;
    line-height: 16px;
    text-transform: uppercase;
    color: var(--brand-purple);
  }
  .person__name {
    margin-top: 26px;
    font-size: 18px;
    letter-spacing: 0.2px;
    text-transform: uppercase;
  }
  .person__role {
    margin-top: 4px;
    font-size: 12px;
    color: var(--ink-soft);
  }
  .contact {
    margin-top: 26px;
    font-size: 12px;
    line-height: 17px;
    color: var(--ink-soft);
  }
</style>
</head>
<body>
<main class="canvas">

  <section class="card card--purple">
    <svg class="card__art" viewBox="0 0 520 360" aria-hidden="true">
      <rect width="520" height="360" fill="var(--purple-5)"/>
      <ellipse cx="170" cy="105" rx="470" ry="345" fill="var(--purple-4)"/>
      <ellipse cx="170" cy="105" rx="410" ry="305" fill="var(--purple-3)"/>
      <ellipse cx="170" cy="105" rx="360" ry="272" fill="var(--purple-2)"/>
      <ellipse cx="170" cy="105" rx="324" ry="250" fill="var(--purple-1)"/>
      <ellipse cx="170" cy="105" rx="308" ry="236" fill="var(--ring-grey)"/>
      <ellipse cx="170" cy="105" rx="300" ry="228" fill="var(--card-white)"/>
    </svg>
    <div class="card__content">
      <div class="brand">
        <span class="brand__dot"></span>
        <span class="brand__name">Continental Hoop Invitational</span>
      </div>
      <div class="person__name">Dorian Pelkey</div>
      <div class="person__role">Project Director</div>
      <div class="contact">
        dorian@hoopinvitational.net<br>
        +65 83147092<br>
        www.hoopinvitational.net<br>
        47 Marbury Lane, #06-11<br>
        Singapore 915274
      </div>
    </div>
  </section>

  <section class="card card--gold">
    <svg class="card__art" viewBox="0 0 520 360" aria-hidden="true">
      <rect width="520" height="360" fill="var(--gold-5)"/>
      <ellipse cx="170" cy="105" rx="470" ry="345" fill="var(--gold-4)"/>
      <ellipse cx="170" cy="105" rx="410" ry="305" fill="var(--gold-3)"/>
      <ellipse cx="170" cy="105" rx="360" ry="272" fill="var(--gold-2)"/>
      <ellipse cx="170" cy="105" rx="324" ry="250" fill="var(--gold-1)"/>
      <ellipse cx="170" cy="105" rx="308" ry="236" fill="var(--ring-grey)"/>
      <ellipse cx="170" cy="105" rx="300" ry="228" fill="var(--card-white)"/>
    </svg>
    <div class="card__content">
      <div class="brand">
        <span class="brand__dot"></span>
        <span class="brand__name">Continental Hoop Invitational</span>
      </div>
      <div class="person__name">Dorian Pelkey</div>
      <div class="person__role">Project Director</div>
      <div class="contact">
        dorian@hoopinvitational.net<br>
        +65 83147092<br>
        www.hoopinvitational.net<br>
        47 Marbury Lane, #06-11<br>
        Singapore 915274
      </div>
    </div>
  </section>

</main>
</body>
</html>
```